BrewDune Lane.

I want the full logo on one side. And the other side the card if right Ralf the logo the left half orange like the car in the logo color with Lorena J Torvand
Founder and CEO
Email symbol then ltorvand@brewdunelanex.com
Www symbol. Then Brewdunelanex.com
Phone symbol then 555-214-BREW
The very bottom would like Brew Dune Lane is a division of Tumbler Treks. LLC

```html
<!DOCTYPE html>
<html lang="en">
<head>
<meta charset="utf-8">
<title>Brew Dune Lane — Business Card</title>
<link rel="stylesheet" href="https://fonts.googleapis.com/css2?family=Rokkitt:wght@700&family=Didact+Gothic&display=swap">
<style>
  :root {
    --bg: #e9e4dc;
    --card-white: #ffffff;
    --card-dark: #232323;
    --orange: #e8902a;
    --ink: #1f1f1f;
    --light: #ffffff;
  }
  * { margin: 0; padding: 0; box-sizing: border-box; }
  html, body { width: 1200px; height: 1200px; overflow: hidden; }
  body { background: var(--bg); position: relative; font-family: "Didact Gothic", sans-serif; }

  .card {
    position: absolute;
    left: 150px;
    width: 903px;
    height: 516px;
    overflow: hidden;
    background: var(--card-dark);
    box-shadow: 0 6px 14px rgba(0,0,0,0.25);
  }
  .card-front { top: 54px; border-radius: 0 60px 0 60px; }
  .card-back  { top: 614px; border-radius: 60px 0 60px 0; }

  .front-top {
    position: absolute; left: 0; top: 0; width: 100%; height: 266px;
    background: var(--card-white);
  }
  .accent-band {
    position: absolute; left: 126px; top: 243px; width: 670px; height: 23px;
    background: var(--orange); border-radius: 23px 23px 0 0;
  }
  .brand-name {
    position: absolute;
    font-family: "Rokkitt", serif; font-weight: 700;
    white-space: nowrap; transform: translateX(-50%);
    letter-spacing: 1px; line-height: 1;
  }
  .brand-front { left: 209px; top: 146px; font-size: 30px; color: var(--ink); }
  .brand-back  { left: 451px; top: 268px; font-size: 54px; color: var(--light); }

  .person-name {
    position: absolute; left: 520px; top: 110px;
    font-family: "Rokkitt", serif; font-weight: 700; font-size: 42px;
    color: var(--ink); text-shadow: 2px 2px 0 #f6cfa1; white-space: nowrap;
  }
  .person-title {
    position: absolute; left: 520px; top: 162px;
    font-size: 21px; color: var(--ink);
    padding-bottom: 3px; border-bottom: 2px solid var(--orange);
  }

  .contact-icons { position: absolute; left: 400px; top: 282px; }
  .rule { position: absolute; height: 1.5px; background: var(--light); }
  .contact-list {
    position: absolute; left: 0; width: 100%; top: 328px;
    text-align: center; color: var(--light); font-size: 22px; line-height: 28px;
  }
  .division-note {
    position: absolute; left: 0; width: 100%; top: 436px;
    text-align: center; color: var(--light); font-size: 18px; line-height: 24px;
  }
</style>
</head>
<body>
  <section class="card card-front">
    <div class="front-top"></div>
    <div class="accent-band"></div>
    <div class="brand-name brand-front">BREW DUNE LANE</div>
    <div class="person-name">Lorena J Torvand</div>
    <div class="person-title">Founder and CEO</div>

    <div class="rule" style="left:249px; top:297px; width:139px;"></div>
    <div class="rule" style="left:516px; top:297px; width:140px;"></div>
    <svg class="contact-icons" width="104" height="32" viewBox="0 0 104 32">
      <circle cx="16" cy="16" r="15" fill="var(--orange)" stroke="#fff" stroke-width="1.5"/>
      <path d="M10 9 q-2 2 0 6 q4 7 9 9 q3 1 5-1 l-3-3 q-1 1-2 0 q-3-2-5-5 q-1-1 0-2 z" fill="#1f1f1f"/>
      <circle cx="52" cy="16" r="15" fill="var(--orange)" stroke="#fff" stroke-width="1.5"/>
      <rect x="43" y="10" width="18" height="12" fill="none" stroke="#1f1f1f" stroke-width="1.6"/>
      <path d="M43 10 l9 7 l9 -7" fill="none" stroke="#1f1f1f" stroke-width="1.6"/>
      <circle cx="88" cy="16" r="15" fill="var(--orange)" stroke="#fff" stroke-width="1.5"/>
      <circle cx="88" cy="16" r="9" fill="none" stroke="#1f1f1f" stroke-width="1.6"/>
      <ellipse cx="88" cy="16" rx="4" ry="9" fill="none" stroke="#1f1f1f" stroke-width="1.4"/>
      <path d="M79 16 h18 M80.5 11.5 h15 M80.5 20.5 h15" stroke="#1f1f1f" stroke-width="1.2"/>
    </svg>

    <div class="contact-list">
      <div>555-214-BREW</div>
      <div>ltorvand@brewdunelanex.com</div>
      <div>brewdunelanex.com</div>
    </div>
    <div class="rule" style="left:247px; top:424px; width:410px;"></div>
    <div class="division-note">
      <div>Brew Dune Lane is a division of</div>
      <div>Tumbler Treks, LLC</div>
    </div>
  </section>

  <section class="card card-back">
    <div class="brand-name brand-back">BREW DUNE LANE</div>
  </section>
</body>
</html>
```